Professional Home Buyer business card needed

I need a pretty straight forward business card designed. We help people that NEED to sell their homes solve problems. We perform all types of Real Estate transactions including flip, wholesale, investment, rental property and multi family. The card will mainly be used to give to prospective Sellers but will also be given to Real Estate Investors as well. It should professional and very easy to read, most clients are older people.

Target Market(s)

Distressed home sellers as well as Real Estate investors

Industry/Entity Type

Real Estate

Contact Information for Business Card

should be a professional layout

Colors
ec1f27
ffffff
000000

Requirements
Must have
• Large logo on back and smaller one on front. should utilize Red, white, and black.
• I am thinking of using a soft touch coating on the card so keep that in mind.
• Contact info should be very easy to read, think older clients.
Nice to have
• I would like to see a design with rounded corners on the card
Should not have
• pictures of homes or other home graphics.

```html
<!DOCTYPE html>
<html lang="en">
<head>
<meta charset="utf-8">
<title>Crestline Home Buyers – Business Card</title>
<link href="https://fonts.googleapis.com/css2?family=Arimo:wght@400;700&display=swap" rel="stylesheet">
<style>
  :root {
    --brand-red: #ec1f27;
    --brand-white: #ffffff;
    --brand-black: #000000;
    --paper-grey: #f1f1f1;
    --stage: #dcd9d3;
  }
  * { box-sizing: border-box; margin: 0; padding: 0; }
  html, body {
    width: 1200px; height: 780px; overflow: hidden;
    background: var(--stage);
    font-family: "Arimo", Arial, sans-serif;
  }
  .sheet { position: relative; width: 1200px; height: 780px; }

  .card {
    position: absolute; top: 240px;
    width: 520px; height: 297px;
    border-radius: 18px; overflow: hidden;
    box-shadow: 0 10px 28px rgba(0,0,0,.25);
  }
  .card--front { left: 50px; background: var(--brand-black); }
  .card--back  { left: 630px; background: linear-gradient(135deg, var(--brand-white), var(--paper-grey)); }

  .card__swoosh { position: absolute; inset: 0; width: 100%; height: 100%; }

  /* company name */
  .brand-name {
    position: absolute; display: flex; align-items: center; gap: 8px;
    font-family: "Arimo", Arial, sans-serif; font-weight: 700;
    color: var(--brand-black); white-space: nowrap; line-height: 1;
  }
  .brand-name__square { background: var(--brand-red); flex: none; }

  .card--front .brand-name { left: 22px; top: 104px; font-size: 17px; }
  .card--front .brand-name__square { width: 11px; height: 11px; }

  .card--back .brand-name {
    left: 50%; top: 50%; transform: translate(-50%, -50%);
    font-size: 34px; gap: 14px;
  }
  .card--back .brand-name__square { width: 20px; height: 20px; }

  /* contact block */
  .contact {
    position: absolute; right: 22px; top: 30px;
    text-align: right; color: var(--brand-white);
  }
  .contact__name { font-size: 19px; font-weight: 700; letter-spacing: .5px; text-transform: uppercase; }
  .contact__role { font-size: 14px; color: var(--brand-red); margin-bottom: 20px; }
  .contact__address { font-size: 13px; line-height: 1.35; margin-bottom: 14px; }
  .contact__lines { list-style: none; }
  .contact__line {
    display: flex; justify-content: flex-end; align-items: center; gap: 8px;
    font-size: 13.5px; line-height: 1; margin-bottom: 9px;
  }
  .contact__icon { width: 17px; height: 17px; flex: none; }
</style>
</head>
<body>
<main class="sheet">

  <!-- Front of card -->
  <section class="card card--front" aria-label="Business card front">
    <svg class="card__swoosh" viewBox="0 0 520 297" preserveAspectRatio="none" aria-hidden="true">
      <path d="M0 0 H312 C265 120 215 225 130 297 H0 Z" fill="var(--brand-white)"/>
      <path d="M312 0 C300 130 260 230 205 297 H130 C215 225 265 120 312 0 Z" fill="var(--brand-red)"/>
    </svg>

    <p class="brand-name">
      <span class="brand-name__square"></span>
      <span>Crestline Home Buyers</span>
    </p>

    <div class="contact">
      <p class="contact__name">Dana Whitfield</p>
      <p class="contact__role">Owner</p>
      <p class="contact__address">PO Box 456, Main Street<br>3rd Avenue, Arizona 85001</p>
      <ul class="contact__lines">
        <li class="contact__line">
          <span>555.010.2468</span>
          <svg class="contact__icon" viewBox="0 0 20 20" aria-hidden="true">
            <circle cx="10" cy="10" r="10" fill="var(--brand-red)"/>
            <path d="M7 5.5 l2 2.2 -1 1.3 c.8 1.5 1.7 2.4 3 3 l1.3-1 2.2 2 -1.2 1.5 c-3.5-.5-6.4-3.4-7-7z" fill="var(--brand-white)"/>
          </svg>
        </li>
        <li class="contact__line">
          <span>hello@crestlinehomes.com</span>
          <svg class="contact__icon" viewBox="0 0 20 20" aria-hidden="true">
            <circle cx="10" cy="10" r="10" fill="var(--brand-red)"/>
            <rect x="5" y="6.5" width="10" height="7" fill="none" stroke="var(--brand-white)" stroke-width="1.2"/>
            <path d="M5 6.5 L10 10.5 L15 6.5" fill="none" stroke="var(--brand-white)" stroke-width="1.2"/>
          </svg>
        </li>
        <li class="contact__line">
          <span>www.crestlinehomes.com</span>
          <svg class="contact__icon" viewBox="0 0 20 20" aria-hidden="true">
            <circle cx="10" cy="10" r="10" fill="var(--brand-red)"/>
            <circle cx="10" cy="10" r="5" fill="none" stroke="var(--brand-white)" stroke-width="1.1"/>
            <ellipse cx="10" cy="10" rx="2.2" ry="5" fill="none" stroke="var(--brand-white)" stroke-width="1"/>
            <path d="M5 10 H15" stroke="var(--brand-white)" stroke-width="1"/>
          </svg>
        </li>
      </ul>
    </div>
  </section>

  <!-- Back of card -->
  <section class="card card--back" aria-label="Business card back">
    <p class="brand-name">
      <span class="brand-name__square"></span>
      <span>Crestline Home Buyers</span>
    </p>
  </section>

</main>
</body>
</html>
```